Startup internet service provider needs a good facebook ad

Looking for a catchy facebook ad to launch our internet service in Parker, Colorado. Short video or slideshow preferred, still pictures are okay.

https://www.facebook.com/BrimcoreNetworks

www.brimcore-networks.example

Target Market(s)

Parker Colorado

Colors
add136
0255a3

```html
<!DOCTYPE html>
<html lang="en">
<head>
<meta charset="utf-8">
<title>Brimcore Networks – Fast and Reliable Internet</title>
<link rel="stylesheet" href="https://fonts.googleapis.com/css2?family=Poppins:wght@400;500;700&display=swap">
<style>
  :root {
    --brand-green: #add136;
    --brand-blue: #0255a3;
    --photo-light: #3a97dc;
    --photo-deep: #1d3a64;
    --ink: #1a1a1a;
    --white: #ffffff;
    --backdrop: #e9eaea;
  }
  * { box-sizing: border-box; margin: 0; padding: 0; }
  html, body {
    width: 1200px; height: 1200px; overflow: hidden;
    background: var(--backdrop);
    font-family: "Poppins", sans-serif;
  }
  .ad-banner {
    position: absolute; left: 30px; top: 302px;
    width: 1140px; height: 596px;
    overflow: hidden;
  }
  .ad-shapes { position: absolute; inset: 0; width: 100%; height: 100%; }
  .headline {
    position: absolute; left: 50px; top: 28px;
    font-size: 53px; font-weight: 700; line-height: 1;
    letter-spacing: -0.5px; color: var(--brand-blue); white-space: nowrap;
  }
  .subhead {
    position: absolute; left: 51px; top: 82px; width: 460px;
    font-size: 21px; font-weight: 400; line-height: 28px;
    color: var(--brand-blue);
  }
  .feature-list {
    position: absolute; left: 53px; top: 184px; width: 382px;
    list-style: none;
  }
  .feature-list li {
    position: relative; padding-left: 31px; margin-bottom: 4.7px;
    font-size: 19px; line-height: 24px; color: var(--ink);
  }
  .feature-list li svg {
    position: absolute; left: 0; top: 6px; width: 15px; height: 12px;
  }
  .phone-bar {
    position: absolute; left: 0; top: 461px;
    width: 448px; height: 67px;
    background: var(--brand-blue);
    border: 2px solid var(--white); border-left: none;
    border-radius: 0 34px 34px 0;
  }
  .phone-bar svg { position: absolute; left: 54px; top: 17px; width: 30px; height: 30px; }
  .phone-number {
    position: absolute; left: 108px; top: 10px;
    font-size: 41px; font-weight: 700; color: var(--white);
    letter-spacing: 0.5px; line-height: 44px;
  }
  .website {
    position: absolute; left: 62px; top: 545px;
    display: flex; align-items: center; height: 24px;
  }
  .website svg { width: 20px; height: 20px; }
  .website span {
    margin-left: 27px; font-size: 19.5px; font-weight: 700;
    color: #111; letter-spacing: 0.2px;
  }
  .brand-mark {
    position: absolute; left: 729px; top: 62px;
    display: flex; align-items: center; height: 48px;
  }
  .brand-mark .dot {
    width: 46px; height: 46px; border-radius: 50%;
    background: var(--brand-green);
  }
  .brand-mark .name {
    margin-left: 13px; font-size: 31px; font-weight: 400;
    color: var(--white); line-height: 1;
  }
</style>
</head>
<body>
  <section class="ad-banner">
    <svg class="ad-shapes" viewBox="0 0 1788 934" preserveAspectRatio="none">
      <defs>
        <linearGradient id="photo-tone" x1="0" y1="0" x2="0.4" y2="1">
          <stop offset="0" stop-color="var(--photo-light)"/>
          <stop offset="1" stop-color="var(--photo-deep)"/>
        </linearGradient>
      </defs>
      <rect class="base-green" width="1788" height="934" fill="var(--brand-green)"/>
      <path class="text-panel" d="M0 0 H870 C790 200 740 540 796 777 H0 Z" fill="var(--white)"/>
      <path class="photo-ring" d="M1160 0 C905 160 790 470 893 934 H1788 V0 Z" fill="var(--brand-blue)"/>
      <path role="img" aria-label="Aerial photo of a city at dusk with glowing network connection arcs between buildings" d="M1228 0 C960 160 835 470 912 934 H1788 V0 Z" fill="url(#photo-tone)"/>
      <polygon class="divider-accent" points="83,227 270,227 283,240 83,240" fill="var(--brand-green)"/>
      <rect class="divider-line" x="283" y="239" width="434" height="2" fill="var(--brand-blue)"/>
    </svg>

    <div class="brand-mark">
      <span class="dot"></span>
      <span class="name">Brimcore Networks</span>
    </div>

    <h1 class="headline">Fast and Reliable</h1>
    <p class="subhead">internet service designed and catered to meet your needs</p>

    <ul class="feature-list">
      <li><svg viewBox="0 0 14 12"><path d="M1 1 L13 6 L1 11 L5 6 Z" fill="var(--brand-green)"/></svg>Fast and reliable internet service</li>
      <li><svg viewBox="0 0 14 12"><path d="M1 1 L13 6 L1 11 L5 6 Z" fill="var(--brand-green)"/></svg>Real customer support</li>
      <li><svg viewBox="0 0 14 12"><path d="M1 1 L13 6 L1 11 L5 6 Z" fill="var(--brand-green)"/></svg>Less buffering while streaming</li>
      <li><svg viewBox="0 0 14 12"><path d="M1 1 L13 6 L1 11 L5 6 Z" fill="var(--brand-green)"/></svg>Fast web browsing</li>
      <li><svg viewBox="0 0 14 12"><path d="M1 1 L13 6 L1 11 L5 6 Z" fill="var(--brand-green)"/></svg>Gaming without the lag</li>
      <li><svg viewBox="0 0 14 12"><path d="M1 1 L13 6 L1 11 L5 6 Z" fill="var(--brand-green)"/></svg>Wall to wall WiFi coverage</li>
      <li><svg viewBox="0 0 14 12"><path d="M1 1 L13 6 L1 11 L5 6 Z" fill="var(--brand-green)"/></svg>No introductory charges, one constant rate</li>
      <li><svg viewBox="0 0 14 12"><path d="M1 1 L13 6 L1 11 L5 6 Z" fill="var(--brand-green)"/></svg>Simple and easy to read bills</li>
    </ul>

    <div class="phone-bar">
      <svg viewBox="0 0 24 24" aria-hidden="true">
        <path d="M6.6 10.8c1.4 2.8 3.8 5.2 6.6 6.6l2.2-2.2c.3-.3.7-.4 1-.2 1.1.4 2.3.6 3.6.6.6 0 1 .4 1 1V20c0 .6-.4 1-1 1C10.6 21 3 13.4 3 4c0-.6.4-1 1-1h3.5c.6 0 1 .4 1 1 0 1.3.2 2.5.6 3.6.1.3 0 .7-.2 1z" fill="var(--white)"/>
        <path d="M15 3a6 6 0 0 1 6 6M15 6.5a2.5 2.5 0 0 1 2.5 2.5" stroke="var(--white)" stroke-width="1.6" fill="none" stroke-linecap="round"/>
      </svg>
      <span class="phone-number">844-555-0137</span>
    </div>

    <div class="website">
      <svg viewBox="0 0 20 20" aria-hidden="true">
        <circle cx="10" cy="10" r="8.5" fill="#111"/>
        <path d="M1.5 10h17M10 1.5v17M3 6h14M3 14h14" stroke="var(--brand-green)" stroke-width="1.1"/>
        <ellipse cx="10" cy="10" rx="3.8" ry="8.5" fill="none" stroke="var(--brand-green)" stroke-width="1.1"/>
      </svg>
      <span>WWW.BRIMCORE-NETWORKS.EXAMPLE</span>
    </div>
  </section>
</body>
</html>
```